Commercial facility maintenance

I need a card design that helps my salesmen make contact with new clients, our product is facility maintenance and heavy industrial maintenance

```html
<!DOCTYPE html>
<html lang="en">
<head>
<meta charset="utf-8">
<title>Hartwell Millworks – Business Card</title>
<link rel="stylesheet" href="https://fonts.googleapis.com/css2?family=Space+Grotesk:wght@400;500;600&display=swap">
<style>
  :root {
    --backdrop: #8e8e8e;
    --card-dark: #262626;
    --card-dark-mark: #222222;
    --card-light: #ffffff;
    --brand-red: #9b2a30;
    --ink-gray: #555555;
    --rule-gray: #8a8a8a;
    --paper-white: #ffffff;
  }
  * { margin: 0; padding: 0; box-sizing: border-box; }
  html, body {
    width: 1200px; height: 1000px; overflow: hidden;
    background: var(--backdrop);
    font-family: "Space Grotesk", sans-serif;
  }
  .canvas { position: relative; width: 1200px; height: 1000px; }
  .card {
    position: absolute; left: 282px; width: 600px; height: 364px;
    border-radius: 32px; overflow: hidden;
  }
  .card--front { top: 142px; background: var(--card-dark); }
  .card--back { top: 544px; background: var(--card-light); }

  .front-mark {
    position: absolute; left: 262px; top: 6px;
    width: 360px; height: 360px; border-radius: 50%;
    background: var(--card-dark-mark);
  }
  .front-name {
    position: absolute; left: 68px; top: 182px;
    color: var(--paper-white);
    font-weight: 600; font-size: 34px; line-height: 1; letter-spacing: 1px;
    text-transform: uppercase;
  }
  .front-name span { display: block; font-size: 13.5px; letter-spacing: 4.2px; margin-top: 6px; }

  .back-logo {
    position: absolute; left: 88px; top: 112px; width: 156px;
    display: flex; flex-direction: column; align-items: center; gap: 12px;
  }
  .back-logo__dot { width: 70px; height: 70px; border-radius: 50%; background: var(--brand-red); }
  .back-logo__name {
    color: var(--ink-gray); font-weight: 600; font-size: 16px;
    text-align: center; line-height: 1.2; text-transform: uppercase; letter-spacing: 0.5px;
  }
  .divider {
    position: absolute; left: 261px; top: 120px; width: 1.5px; height: 148px;
    background: var(--rule-gray);
  }
  .person { position: absolute; left: 285px; top: 128px; }
  .person__name { color: var(--brand-red); font-weight: 500; font-size: 23px; line-height: 1.1; }
  .person__title { color: var(--ink-gray); font-size: 17px; line-height: 1.3; margin-top: 1px; }
  .contact-list { position: absolute; left: 287px; top: 204px; list-style: none; }
  .contact-list li {
    display: flex; align-items: center; gap: 9px;
    color: var(--ink-gray); font-size: 16.5px; height: 21px;
  }
  .contact-list svg { width: 15px; height: 15px; flex: none; }
</style>
</head>
<body>
<main class="canvas">
  <section class="card card--front" aria-label="Card front">
    <div class="front-mark"></div>
    <p class="front-name">Hartwell<span>Millworks LLC</span></p>
  </section>

  <section class="card card--back" aria-label="Card back">
    <div class="back-logo">
      <div class="back-logo__dot"></div>
      <p class="back-logo__name">Hartwell Millworks</p>
    </div>
    <div class="divider"></div>
    <div class="person">
      <p class="person__name">Name Surname</p>
      <p class="person__title">Title</p>
    </div>
    <ul class="contact-list">
      <li>
        <svg viewBox="0 0 24 24" aria-hidden="true"><path fill="#9b2a30" d="M6.6 10.8a15.1 15.1 0 0 0 6.6 6.6l2.2-2.2c.3-.3.7-.4 1-.2 1.1.4 2.3.6 3.6.6.6 0 1 .4 1 1V20c0 .6-.4 1-1 1A17 17 0 0 1 3 4c0-.6.4-1 1-1h3.5c.6 0 1 .4 1 1 0 1.3.2 2.5.6 3.6.1.3 0 .7-.2 1z"/></svg>
        555-014-2290
      </li>
      <li>
        <svg viewBox="0 0 24 24" aria-hidden="true"><rect x="2" y="5" width="20" height="14" fill="#9b2a30"/><path d="M2.5 5.5 12 13l9.5-7.5M2.5 18.5l7-6.5M21.5 18.5l-7-6.5" stroke="#fff" stroke-width="1.5" fill="none"/></svg>
        hwmills@mail.com
      </li>
      <li>
        <svg viewBox="0 0 24 24" aria-hidden="true"><g fill="none" stroke="#9b2a30" stroke-width="2"><circle cx="12" cy="12" r="9.5"/><ellipse cx="12" cy="12" rx="4" ry="9.5"/><path d="M2.5 12h19M4 7h16M4 17h16"/></g></svg>
        hartwellmillworksllc.com
      </li>
    </ul>
  </section>
</main>
</body>
</html>
```